Coding for One Page Website

Website was previously designed using Craftmeadow (attached). I now need it coded so I can publish using Webtulip.

Company: Amber Ridge Funds

Reason: Still waiting for exactly what I need.

Industry/Entity Type

It Company

```html
<!DOCTYPE html>
<html lang="en">
<head>
<meta charset="utf-8">
<title>Amber Ridge Funds</title>
<link href="https://fonts.googleapis.com/css2?family=Open+Sans:wght@400;600&display=swap" rel="stylesheet">
<style>
  :root {
    --blue-light: #0b7dd1;
    --blue-dark: #0a5a9c;
    --button-blue: #0a79cc;
    --ink: #1a1a1a;
    --muted: #7b7b7b;
    --white: #ffffff;
    --rule: rgba(255,255,255,0.35);
    --hero-tone-a: #5a5450;
    --hero-tone-b: #d9cfc4;
    --illus-a: #e9eef3;
    --illus-b: #c9a27a;
  }
  * { box-sizing: border-box; margin: 0; padding: 0; }
  html, body {
    width: 1200px; height: 655px; overflow: hidden;
    background: var(--white);
    font-family: "Open Sans", Arial, sans-serif;
  }
  .page { position: relative; width: 1200px; height: 655px; overflow: hidden; }

  .hero-strip {
    position: absolute; left: 0; top: 0; width: 1200px; height: 24px;
    background: linear-gradient(90deg, var(--hero-tone-b) 0%, #efe9e2 30%, var(--hero-tone-a) 48%, #e8e1d9 60%, var(--hero-tone-b) 100%);
  }

  .features {
    position: absolute; left: 84px; top: 24px; width: 1026px; height: 164px;
    display: flex;
  }
  .feature {
    flex: 1; color: var(--white); text-align: center;
    padding: 8px 18px 0;
  }
  .feature:nth-child(odd) { background: var(--blue-light); }
  .feature:nth-child(even) { background: var(--blue-dark); }
  .feature-icon { display: block; margin: 0 auto; width: 36px; height: 32px; }
  .feature-title {
    font-size: 14.5px; font-weight: 600; letter-spacing: 0.2px;
    margin-top: 6px; padding-bottom: 6px;
    border-bottom: 1px solid var(--rule);
    width: 136px; margin-left: auto; margin-right: auto;
  }
  .feature-text {
    font-size: 12.5px; font-weight: 600; line-height: 16.5px;
    margin-top: 12px;
  }

  .about {
    position: absolute; left: 0; top: 222px; width: 1200px; text-align: center;
  }
  .about-heading { font-size: 19px; font-weight: 400; color: var(--ink); letter-spacing: 0.3px; }
  .about-sub { font-size: 14px; font-weight: 400; color: var(--ink); margin-top: 13px; letter-spacing: 0.2px; }
  .about-rule { width: 46px; height: 2px; background: var(--button-blue); margin: 16px auto 0; }
  .about-text {
    width: 1060px; margin: 17px auto 0;
    font-size: 12.8px; line-height: 16.5px; color: var(--muted);
  }
  .read-more {
    display: inline-block; margin-top: 22px;
    width: 96px; height: 27px; line-height: 27px; border-radius: 14px;
    background: var(--button-blue); color: var(--white);
    font-size: 12.5px; font-weight: 600; text-decoration: none;
  }

  .illustration {
    position: absolute; left: 438px; top: 420px; width: 320px; height: 235px;
    background: linear-gradient(180deg, var(--illus-a) 0%, #d6dbe0 70%, var(--illus-b) 100%);
    border-radius: 6px 6px 0 0;
  }
</style>
</head>
<body>
<div class="page">
  <div class="hero-strip" role="img" aria-label="Office photograph banner"></div>

  <section class="features">
    <div class="feature">
      <svg class="feature-icon" viewBox="0 0 36 32" fill="none" stroke="#fff" stroke-width="1.8">
        <rect x="3" y="9" width="24" height="16" rx="2"/>
        <rect x="9" y="5" width="24" height="16" rx="2" fill="var(--blue-light)"/>
        <line x1="9" y1="10" x2="33" y2="10"/>
        <line x1="13" y1="16" x2="20" y2="16"/>
      </svg>
      <h3 class="feature-title">NEW TO CARDS?</h3>
      <p class="feature-text">Lorem Ipsum is simply dummy text of the printing and typesetting industry. Lorem Ipsum has been...</p>
    </div>
    <div class="feature">
      <svg class="feature-icon" viewBox="0 0 36 32" fill="#fff">
        <polygon points="4,10 14,2 14,7 26,7 26,13 14,13 14,18"/>
        <polygon points="32,22 22,14 22,19 10,19 10,25 22,25 22,30"/>
      </svg>
      <h3 class="feature-title">SWITCH &amp; SAVE</h3>
      <p class="feature-text">Lorem Ipsum is simply dummy text of the printing and typesetting industry. Lorem Ipsum has been...</p>
    </div>
    <div class="feature">
      <svg class="feature-icon" viewBox="0 0 36 32" fill="none" stroke="#fff" stroke-width="2">
        <path d="M9 16 V13 A9 9 0 0 1 27 13 V16"/>
        <rect x="7" y="14" width="4" height="7" rx="1.5" fill="#fff"/>
        <rect x="25" y="14" width="4" height="7" rx="1.5" fill="#fff"/>
        <path d="M27 21 Q27 25 21 25"/>
        <path d="M6 31 Q6 25 18 25 Q30 25 30 31 Z" fill="#fff" stroke="none"/>
      </svg>
      <h3 class="feature-title">CUSTOMER SUPPORT</h3>
      <p class="feature-text">Lorem Ipsum is simply dummy text of the printing and typesetting industry. Lorem Ipsum has been...</p>
    </div>
    <div class="feature">
      <svg class="feature-icon" viewBox="0 0 36 32" fill="none" stroke="#fff" stroke-width="1.8">
        <rect x="3" y="3" width="30" height="21" rx="1.5"/>
        <line x1="14" y1="29" x2="22" y2="29"/>
        <line x1="18" y1="24" x2="18" y2="29"/>
        <polygon points="12,8 12,18 15,15 18,20 20,19 17,14 21,14" fill="#fff" stroke="none"/>
      </svg>
      <h3 class="feature-title">APPLY ONLINE</h3>
      <p class="feature-text">Lorem Ipsum is simply dummy text of the printing and typesetting industry. Lorem Ipsum has been...</p>
    </div>
  </section>

  <section class="about">
    <h2 class="about-heading">ABOUT US</h2>
    <h3 class="about-sub">AMBER RIDGE FUNDS</h3>
    <div class="about-rule"></div>
    <p class="about-text">Lorem Ipsum is simply dummy text of the printing and typesetting industry. Llorem Ipsum has been the Industry's standard dummy text ever since the 1500s, when an unknown printer took a gallery of type nad scrambled it to make a type specimen book. It has survived not only five centuries.</p>
    <a class="read-more" href="#">Read More</a>
  </section>

  <div class="illustration" role="img" aria-label="Illustration of a desktop computer on a desk with hands holding a card, a calculator and a coin, surrounded by gears"></div>
</div>
</body>
</html>
```